Online-Marketing-Material für Reinigungsunternehmen
Zielgruppe
Wir sind ein seit Jahresanfang bestehende Reinigungsunternehmen.
Unsere Schwerpunkte liegen auf Treppenhausreinigung und Büroreinigung.
Die Anzeige soll auf Facebook / Instagram als Werbung angezeigt werden.
Kunden sind sowohl Unternehmer sowie auch Privathaushalte und Hausverwaltungen.
www.kolvaputz.de
Aufgabenstellung
Es darf gerne Modern und verspielt sein. Es soll und darf nicht billig wirken.
Wir haben auch ein Maskottchen. Es muss aber nicht auf die Anzeige mit drauf!

```html
<!DOCTYPE html>
<html lang="de">
<head>
<meta charset="UTF-8">
<title>Kolva Putz – Anzeige</title>
<link rel="stylesheet" href="https://fonts.googleapis.com/css2?family=Poppins:wght@400;500;600;700;800&display=swap">
<style>
  :root{
    --canvas:#ffffff;
    --panel-top:#2a2a26;
    --panel-bottom:#6a6a65;
    --text-light:#ffffff;
    --text-dark:#3a3a38;
    --accent-green:#5db52c;
    --photo-wall:#6a6a65;
    --photo-shade:#5e5650;
    --photo-brown:#6e5444;
    --photo-floor:#cfc6bb;
  }
  *{margin:0;padding:0;box-sizing:border-box}
  html,body{width:1200px;height:1200px;overflow:hidden;background:var(--canvas)}
  .ad{position:relative;width:1200px;height:1200px;font-family:'Poppins',sans-serif;color:var(--text-light)}
  .ad-shape{position:absolute;inset:0}
  .brand{position:absolute;left:470px;top:168px;width:380px;display:flex;align-items:center;gap:22px}
  .brand-square{flex:none;width:46px;height:46px;background:var(--text-light)}
  .brand-text{display:flex;flex-direction:column}
  .brand-name{font-size:56px;font-weight:700;line-height:0.95}
  .brand-owner{margin-top:10px;font-size:19px;font-weight:400}
  .headline{position:absolute;left:300px;width:650px;text-align:center;text-transform:uppercase}
  .headline-intro{top:368px;font-size:36px;font-weight:800;line-height:1.12}
  .headline-main{top:465px;font-size:92px;font-weight:800;line-height:0.9;letter-spacing:-1px}
  .services{position:absolute;top:652px;left:300px;width:650px;list-style:none;text-align:center;font-size:26px;font-weight:500;line-height:1.24}
  .services li{display:flex;align-items:center;justify-content:center;gap:8px}
  .services svg{width:18px;height:18px}
  .sparkles{position:absolute;inset:0;pointer-events:none}
  .cta{position:absolute;left:551px;top:1044px;width:190px;height:39px;background:#fff;border-radius:3px;display:flex;align-items:center;justify-content:space-between;padding:0 14px;color:var(--text-dark);font-size:17px;font-weight:700;text-decoration:none}
  .cta svg{width:14px;height:16px}
</style>
</head>
<body>
<div class="ad">
  <svg class="ad-shape" viewBox="0 0 1200 1200" width="1200" height="1200">
    <defs>
      <linearGradient id="panelGradient" x1="0" y1="0" x2="0" y2="1">
        <stop offset="0" stop-color="var(--panel-top)"/>
        <stop offset="0.64" stop-color="var(--panel-bottom)"/>
        <stop offset="1" stop-color="var(--panel-bottom)"/>
      </linearGradient>
      <linearGradient id="photoGradient" x1="0" y1="0" x2="0" y2="1">
        <stop offset="0" stop-color="var(--photo-wall)"/>
        <stop offset="0.3" stop-color="var(--photo-shade)"/>
        <stop offset="0.55" stop-color="var(--photo-brown)"/>
        <stop offset="0.8" stop-color="#a8998b"/>
        <stop offset="1" stop-color="var(--photo-floor)"/>
      </linearGradient>
    </defs>
    <polygon class="panel" points="286,121 921,49 839,1125 458,1125" fill="url(#panelGradient)"/>
    <polygon class="photo" role="img" aria-label="Foto: brauner Welpe neben umgestoßenem Blumentopf mit Farn und verstreuter Erde"
      points="391.5,737 868.6,737 839,1125 458,1125" fill="url(#photoGradient)"/>
  </svg>

  <svg class="sparkles" viewBox="0 0 1200 1200" width="1200" height="1200" aria-hidden="true">
    <defs>
      <radialGradient id="sparkleGlow">
        <stop offset="0" stop-color="#fff" stop-opacity="0.55"/>
        <stop offset="1" stop-color="#fff" stop-opacity="0"/>
      </radialGradient>
      <g id="sparkle">
        <circle r="18" fill="url(#sparkleGlow)"/>
        <path d="M0 -14 L2 -2 L14 0 L2 2 L0 14 L-2 2 L-14 0 L-2 -2 Z" fill="#fff"/>
      </g>
    </defs>
    <use href="#sparkle" transform="translate(830 455) scale(0.6)"/>
    <use href="#sparkle" transform="translate(475 500) scale(0.8)"/>
    <use href="#sparkle" transform="translate(775 503) scale(0.9)"/>
    <use href="#sparkle" transform="translate(427 572) scale(0.8)"/>
    <use href="#sparkle" transform="translate(657 586) scale(0.6)"/>
    <use href="#sparkle" transform="translate(822 586) scale(1.1)"/>
  </svg>

  <header class="brand">
    <span class="brand-square"></span>
    <div class="brand-text">
      <div class="brand-name">Kolva<br>Putz</div>
      <p class="brand-owner">Inh. Rafael Moreno</p>
    </div>
  </header>

  <h2 class="headline headline-intro">Wir schenken<br>Ihrem Objekt</h2>
  <h1 class="headline headline-main">Neuen<br>Glanz</h1>

  <ul class="services">
    <li><svg viewBox="0 0 18 18"><path d="M2 9 L7 14 L16 4" fill="none" stroke="#fff" stroke-width="2.8"/></svg>Treppenhausreinigung</li>
    <li><svg viewBox="0 0 18 18"><path d="M2 9 L7 14 L16 4" fill="none" stroke="#fff" stroke-width="2.8"/></svg>Büroreinigung</li>
  </ul>

  <a class="cta">Jetzt anfragen<svg viewBox="0 0 14 16"><path d="M3 2 L10 8 L3 14" fill="none" stroke="var(--accent-green)" stroke-width="3.2"/></svg></a>
</div>
</body>
</html>
```